construction company offering modern and striking homes and apartments

I need a card design for my new construction company called Talmont Constructions (vic) Pty Ltd.
We build everything from multi home development sites to modern and edgy apartment complexes.
I am open to any colors used as long as it stands out and doesn't look cheap. I want the final design to show my prospective clients I am a professional construction company

Industry/Entity Type

Construction

```html
<!DOCTYPE html>
<html lang="en">
<head>
<meta charset="utf-8">
<title>Talmont Constructions – Business Card</title>
<link rel="stylesheet" href="https://fonts.googleapis.com/css2?family=Josefin+Sans:wght@300;400&display=swap">
<style>
  :root {
    --page-bg: #e4e4e2;
    --card-bg: #ffffff;
    --ink: #1e1c1c;
    --mark: #231f1f;
    --badge-navy: #1f2c5c;
    --badge-green: #2f8a4a;
    --shadow: rgba(0, 0, 0, 0.18);
  }
  * { box-sizing: border-box; margin: 0; padding: 0; }
  html, body {
    width: 1200px;
    height: 872px;
    overflow: hidden;
    background: var(--page-bg);
    font-family: "Josefin Sans", sans-serif;
    color: var(--ink);
  }
  .sheet {
    position: relative;
    width: 1200px;
    height: 872px;
  }
  .card {
    position: absolute;
    top: 136px;
    width: 340px;
    height: 600px;
    background: var(--card-bg);
    box-shadow: 0 8px 26px var(--shadow);
  }
  .card--front { left: 180px; }
  .card--back  { left: 680px; }

  /* Front */
  .partner-badges {
    position: absolute;
    top: 18px;
    right: 18px;
    display: flex;
    gap: 8px;
    align-items: center;
  }
  .partner-badge--rect {
    width: 58px;
    height: 36px;
    background: var(--badge-navy);
  }
  .partner-badge--round {
    width: 36px;
    height: 36px;
    border-radius: 50%;
    background: var(--badge-green);
  }
  .front-disc {
    position: absolute;
    top: 92px;
    left: 16px;
    width: 212px;
    height: 212px;
    border-radius: 50%;
    background: var(--mark);
  }
  .company-name {
    position: absolute;
    top: 338px;
    left: 30px;
    font-weight: 300;
    font-size: 27px;
    line-height: 1.02;
    letter-spacing: 1.5px;
    text-transform: uppercase;
  }
  .contact-list {
    position: absolute;
    top: 436px;
    left: 30px;
    list-style: none;
    font-weight: 300;
    font-size: 16px;
    line-height: 22px;
    letter-spacing: 0.6px;
  }
  .contact-item {
    display: flex;
    align-items: flex-start;
    gap: 12px;
  }
  .contact-icon {
    width: 14px;
    height: 22px;
    flex: none;
  }
  .contact-icon--blank { visibility: hidden; }

  /* Back */
  .back-disc {
    position: absolute;
    top: 42px;
    left: 90px;
    width: 96px;
    height: 96px;
    border-radius: 50%;
    background: var(--mark);
  }
  .back-name {
    position: absolute;
    top: 132px;
    left: 198px;
    writing-mode: vertical-rl;
    font-weight: 300;
    font-size: 22px;
    line-height: 1.05;
    letter-spacing: 2px;
    text-transform: uppercase;
  }
</style>
</head>
<body>
<main class="sheet">

  <section class="card card--front" aria-label="Card front">
    <div class="partner-badges">
      <div class="partner-badge--rect" aria-hidden="true"></div>
      <div class="partner-badge--round" aria-hidden="true"></div>
    </div>
    <div class="front-disc" aria-hidden="true"></div>
    <h1 class="company-name">Talmont<br>Constructions</h1>
    <ul class="contact-list">
      <li class="contact-item">
        <svg class="contact-icon contact-icon--blank" viewBox="0 0 14 22"></svg>
        <span>www.yourwebpage.com</span>
      </li>
      <li class="contact-item">
        <svg class="contact-icon" viewBox="0 0 14 22" aria-hidden="true">
          <rect x="1" y="6" width="12" height="8" fill="none" stroke="#1e1c1c" stroke-width="1.4"/>
          <path d="M5 17h4M7 14v3" stroke="#1e1c1c" stroke-width="1.4"/>
        </svg>
        <span>info@talmont.com</span>
      </li>
      <li class="contact-item">
        <svg class="contact-icon" viewBox="0 0 14 22" aria-hidden="true">
          <rect x="1" y="6" width="12" height="9" fill="#1e1c1c"/>
          <path d="M1 6l6 5 6-5" fill="none" stroke="#fff" stroke-width="1.2"/>
        </svg>
        <span>27 Ridge Lane</span>
      </li>
      <li class="contact-item">
        <svg class="contact-icon" viewBox="0 0 14 22" aria-hidden="true">
          <path d="M7 3a4.5 4.5 0 0 0-4.5 4.5C2.5 11 7 16 7 16s4.5-5 4.5-8.5A4.5 4.5 0 0 0 7 3z" fill="#1e1c1c"/>
          <circle cx="7" cy="7.5" r="1.6" fill="#fff"/>
        </svg>
        <span>Norwood Park vic 3081</span>
      </li>
    </ul>
  </section>

  <section class="card card--back" aria-label="Card back">
    <div class="back-disc" aria-hidden="true"></div>
    <p class="back-name">Talmont<br>Constructions</p>
  </section>

</main>
</body>
</html>
```